Looking for an amazing business card for a thriving DJ business

We need a business card design for a DJ company based in South Florida. The DJ company specializes in weddings, parties, bar mitzvahs, corporate events, proms, and reunions. We are looking for a modern, simple business card design. The card should state DJ Marlow K.
Updates

The name on the card should be DJ Marlow K

Industry/Entity Type

Entertainment Industry

Contact Information for Business Card

DJ Marlow K
512.447.2086
atxdjmarlowk@quellmail.com
https://www.facebook.com/DjMarlowK/
https://www.instagram.com/djmarlow.k/
www.djmarlowk.net

Font styles to use
Serif
Sans Serif

Requirements
Must have
• My business card has to be awesome.
Should not have
• The card has to have personality.

```html
<!DOCTYPE html>
<html lang="en">
<head>
<meta charset="utf-8">
<title>DJ Marlow K — Business Card</title>
<link href="https://fonts.googleapis.com/css2?family=Open+Sans:wght@400;700&display=swap" rel="stylesheet">
<style>
  :root {
    --page: #2a2a2a;
    --card-dark: #1b1b1b;
    --card-panel: #232323;
    --card-textured: #161616;
    --gold: #c9a04e;
    --gold-band: #6b5a3a;
    --silver-light: #e6e6e6;
    --silver-dark: #555555;
    --badge: #ffffff;
    --badge-ink: #4a4a4a;
    --text-light: #f2f2f2;
  }
  * { box-sizing: border-box; margin: 0; padding: 0; }
  html, body { width: 1200px; height: 1200px; overflow: hidden; }
  body {
    background: var(--page);
    font-family: "Open Sans", Arial, sans-serif;
    display: flex;
    flex-direction: column;
    align-items: center;
    justify-content: center;
    gap: 60px;
  }
  .card {
    position: relative;
    width: 840px;
    height: 480px;
    overflow: hidden;
    box-shadow: 0 12px 30px rgba(0,0,0,.55);
  }
  /* Back side */
  .card-back { background: var(--card-textured); }
  .card-back .band {
    position: absolute;
    left: 0; right: 0;
    top: 150px; height: 150px;
    background: var(--gold-band);
  }
  .badge {
    position: absolute;
    border-radius: 50%;
    background: var(--badge);
    display: flex;
    align-items: center;
    justify-content: center;
    text-align: center;
    gap: 8px;
  }
  .badge-name {
    font-family: "Open Sans", Arial, sans-serif;
    font-weight: 700;
    color: var(--badge-ink);
    line-height: 1.15;
  }
  .card-back .badge {
    width: 210px; height: 210px;
    left: 315px; top: 120px;
    flex-direction: column;
  }
  .card-back .badge-name { font-size: 26px; }
  .badge-dot {
    width: 14px; height: 14px;
    border-radius: 50%;
    background: var(--gold);
  }
  /* Front side */
  .card-front { background: var(--card-panel); }
  .card-front .arcs { position: absolute; inset: 0; }
  .card-front .badge {
    width: 230px; height: 230px;
    left: 548px; top: 60px;
    flex-direction: column;
  }
  .card-front .badge-name { font-size: 28px; }
  .name-marker {
    position: absolute;
    left: 0; top: 205px;
    width: 30px; height: 40px;
    background: var(--gold);
  }
  .name {
    position: absolute;
    left: 60px; top: 196px;
    font-size: 40px;
    font-weight: 700;
    color: var(--gold);
    letter-spacing: .5px;
  }
  .contacts {
    position: absolute;
    left: 150px; top: 320px;
    list-style: none;
    display: flex;
    flex-direction: column;
    gap: 6px;
  }
  .contact {
    display: flex;
    align-items: center;
    gap: 10px;
    font-size: 22px;
    color: var(--text-light);
    line-height: 1.2;
  }
  .icon {
    width: 24px; height: 24px;
    background: var(--gold);
    border-radius: 3px;
    flex: none;
  }
  .icon svg { display: block; width: 24px; height: 24px; }
  .social-pair { display: flex; gap: 6px; }
</style>
</head>
<body>

  <section class="card card-back" aria-label="Card back">
    <div class="band"></div>
    <div class="badge">
      <span class="badge-dot"></span>
      <span class="badge-name">Halcyon<br>Beats</span>
    </div>
  </section>

  <section class="card card-front" aria-label="Card front">
    <svg class="arcs" viewBox="0 0 840 480" width="840" height="480" aria-hidden="true">
      <defs>
        <linearGradient id="silver" x1="0" y1="0" x2="1" y2="1">
          <stop offset="0" stop-color="var(--silver-dark)"/>
          <stop offset=".55" stop-color="var(--silver-light)"/>
          <stop offset="1" stop-color="var(--silver-dark)"/>
        </linearGradient>
      </defs>
      <path d="M420 0 C430 190 520 330 640 395 L840 395 L840 0 Z" fill="url(#silver)"/>
      <path d="M445 0 C455 185 545 325 665 385 L840 395 L840 0 Z" fill="var(--card-dark)"/>
      <path d="M470 0 C478 180 570 320 700 372 L840 392 L840 0 Z" fill="var(--gold)"/>
      <path d="M480 0 C488 175 580 310 710 362 L840 380 L840 0 Z" fill="var(--card-textured)"/>
    </svg>
    <div class="badge">
      <span class="badge-dot"></span>
      <span class="badge-name">Halcyon<br>Beats</span>
    </div>

    <span class="name-marker"></span>
    <h1 class="name">DJ Marlow K</h1>

    <ul class="contacts">
      <li class="contact">
        <span class="icon"><svg viewBox="0 0 24 24"><path d="M8 5l3 3-2 2c1 2 3 4 5 5l2-2 3 3-2 3C10 19 5 14 5 7z" fill="#222"/></svg></span>
        512.447.2086
      </li>
      <li class="contact">
        <span class="icon"><svg viewBox="0 0 24 24"><rect x="5" y="7" width="14" height="10" fill="none" stroke="#222" stroke-width="1.8"/><path d="M5 7l7 6 7-6" fill="none" stroke="#222" stroke-width="1.8"/></svg></span>
        atxdjmarlowk@quellmail.com
      </li>
      <li class="contact">
        <span class="icon"><svg viewBox="0 0 24 24"><circle cx="12" cy="12" r="6.5" fill="none" stroke="#222" stroke-width="1.8"/><path d="M5.5 12h13M12 5.5c-3 3.5-3 9.5 0 13M12 5.5c3 3.5 3 9.5 0 13" fill="none" stroke="#222" stroke-width="1.4"/></svg></span>
        www.djmarlowk.net
      </li>
      <li class="contact">
        <span class="social-pair"><span class="icon"></span><span class="icon"></span></span>
        @DjMarlowK
      </li>
    </ul>
  </section>

</body>
</html>
```